Re-design of current business cards

We are updating our website with new colors and layout. Would like to re-design our business cards to co-ordinate. See attached pdf with new Brightwell website colors. We would also like to combine our 2 brands on the one business card. Attached is the new design for our Brightwell website, current business cards, which are one sided, brightwell logo in tiff, .ai for fonts. Brightwell logo font is Optimum, Lanterncove website home page image, Lanterncove brand statics for products which includes the logo for this brand.

Lanterncove brand will stay the dark gray on the website. See attached statics for product and website home page.
Updates

The business cards will be 2 sided. Brightwell Brand on one side and Lanterncove Brand on the other. The colors for Brightwell need to follow the color scheme of the brightwell website pdf I uploaded. The colors are a blue, lighter teal blue and white. Lanterncove needs to follow the dark gray color on files uploaded

Target Market(s)

The trade and consumers

Industry/Entity Type

Home Furnishing

Contact Information for Business Card

We are updating our website with new colors and layout. Would like to re-design our business cards to co-ordinate. We would also like to combine our 2 brands onto 1 2 sided business cards.

Requirements
Must have
• Colors that match our new website, see attached image.
• RGB colors
• navy -#152842
• teal - 98aeb9
• The gray color used for Lanterncove brands.
• ll logos and fonts should stay the same.

```html
<!DOCTYPE html>
<html lang="en">
<head>
<meta charset="utf-8">
<title>Brightwell & Lanterncove Business Card</title>
<link rel="stylesheet" href="https://fonts.googleapis.com/css2?family=Marcellus&family=Lato:wght@400;700&display=swap">
<style>
  :root {
    --backdrop: #ececec;
    --card-white: #f7f7f6;
    --navy: #152842;
    --teal: #98aeb9;
    --divider: #c9c9c9;
    --lantern-gray: #585858;
    --lantern-text: #e6e6e6;
    --lantern-sub: #c4c4c4;
  }
  * { margin: 0; padding: 0; box-sizing: border-box; }
  html, body {
    width: 1200px; height: 1120px; overflow: hidden;
    background: var(--backdrop);
  }
  .sheet {
    width: 1200px; height: 1120px;
    display: flex; flex-direction: column; align-items: center; justify-content: center;
    gap: 80px;
  }
  .card {
    position: relative;
    width: 700px; height: 400px;
    box-shadow: 0 6px 18px rgba(0,0,0,0.12);
  }

  /* Brightwell side */
  .card--brightwell {
    background: var(--card-white);
    display: flex; align-items: center;
  }
  .card--brightwell .accent-band {
    position: absolute; left: 0; right: 0; bottom: 0;
    height: 16px; background: var(--teal);
  }
  .brand-block {
    width: 330px;
    display: flex; flex-direction: column; align-items: center; gap: 10px;
  }
  .brand-mark {
    width: 40px; height: 40px; border-radius: 50%;
    background: var(--teal);
    margin-left: 150px;
  }
  .brand-name {
    font-family: "Marcellus", serif;
    font-size: 42px; letter-spacing: 2px;
    color: var(--navy);
  }
  .divider {
    width: 1px; height: 170px; background: var(--divider);
  }
  .contact-block {
    padding-left: 36px;
    font-family: "Lato", sans-serif;
    color: var(--navy);
    font-size: 16px; line-height: 1.35;
  }
  .contact-name {
    font-weight: 700; font-size: 22px; letter-spacing: 1px;
    color: var(--navy);
  }
  .contact-role { margin-bottom: 2px; }
  .contact-lines { margin-top: 2px; }
  .contact-line { display: flex; align-items: center; gap: 10px; }
  .contact-line svg { width: 14px; height: 14px; flex: none; }
  .contact-line .web strong { color: var(--navy); font-weight: 700; }

  /* Lanterncove side */
  .card--lanterncove {
    background: var(--lantern-gray);
    display: flex; flex-direction: column; justify-content: center;
    padding-left: 70px;
  }
  .lantern-lockup {
    display: inline-flex; flex-direction: column; align-items: flex-end;
    align-self: flex-start;
  }
  .lantern-name {
    font-family: "Marcellus", serif;
    font-size: 68px; letter-spacing: 2px; line-height: 1;
    color: var(--lantern-text);
  }
  .lantern-by {
    font-family: "Marcellus", serif;
    font-size: 15px; letter-spacing: 1px;
    color: var(--lantern-text);
    margin-top: 4px;
  }
  .lantern-tagline {
    font-family: "Lato", sans-serif;
    font-size: 22px; letter-spacing: 1.5px;
    color: var(--lantern-sub);
    margin-top: 8px;
  }
</style>
</head>
<body>
<main class="sheet">
  <section class="card card--brightwell" aria-label="Brightwell side">
    <div class="brand-block">
      <span class="brand-mark"></span>
      <span class="brand-name">BRIGHTWELL</span>
    </div>
    <span class="divider"></span>
    <div class="contact-block">
      <div class="contact-name">MARA ELLISON</div>
      <div class="contact-role">Graphic | Photography Director</div>
      <div>PO Box 412/2710, Linden Ridge RD</div>
      <div>Fairhaven, VIRGINIA 24190</div>
      <div class="contact-lines">
        <div class="contact-line">
          <svg viewBox="0 0 16 16" aria-hidden="true"><path fill="#98aeb9" d="M4 1l3 3-2 2c1 2 3 4 5 5l2-2 3 3-2 3C7 15 1 9 1 3z"/></svg>
          <span>555.210.4830</span>
        </div>
        <div class="contact-line">
          <svg viewBox="0 0 16 16" aria-hidden="true"><rect x="4" y="1" width="8" height="4" fill="#98aeb9"/><rect x="1" y="6" width="14" height="8" rx="1" fill="#98aeb9"/></svg>
          <span>555.210.4867</span>
        </div>
        <div class="contact-line">
          <svg viewBox="0 0 16 16" aria-hidden="true"><rect x="1" y="3" width="14" height="10" fill="none" stroke="#98aeb9" stroke-width="1.5"/><path d="M1 3l7 6 7-6" fill="none" stroke="#98aeb9" stroke-width="1.5"/></svg>
          <span>mellison@brightwell.com</span>
        </div>
        <div class="contact-line">
          <svg viewBox="0 0 16 16" aria-hidden="true"><circle cx="8" cy="8" r="7" fill="none" stroke="#98aeb9" stroke-width="1.5"/><ellipse cx="8" cy="8" rx="3" ry="7" fill="none" stroke="#98aeb9" stroke-width="1.2"/><path d="M1 8h14" stroke="#98aeb9" stroke-width="1.2"/></svg>
          <span class="web">www.<strong>brightwell</strong>.com</span>
        </div>
      </div>
    </div>
    <span class="accent-band"></span>
  </section>

  <section class="card card--lanterncove" aria-label="Lanterncove side">
    <div class="lantern-lockup">
      <div class="lantern-name">LANTERNCOVE</div>
      <div class="lantern-by">by BRIGHTWELL</div>
    </div>
    <div class="lantern-tagline">Discover the luxury of home.</div>
  </section>
</main>
</body>
</html>
```